Comet raiders stall

Design a Comet Raiders themed stall frontage for a food stall attending a Comet Raiders convention. The stall will be situated in a large hall and the design of the frontage needs to attract attendees from far away, hence the design cannot be too busy.

Please use either of the following stall names:
The Drifting Oruvel Kitchen
Iron Cohort Snacks
Quorvane Plaza Eats

Please include a matching menu board to go with the frontage design. Bonus points for designers who can come up with 4 comet raiders themed names for the food items. The stall will be serving individual meal boxes of pork, chicken and vegan options and Combination box of all the items.

Please look at the example image attached of the stall which shows where the branding will be attached.
Dimensions
Top: 3m(w) x 0.5m(H)
Bottom: 3m(w) x 0.9m (H)
Menu Board: 0.5m (W) x 0.9 (H)

```html
<!DOCTYPE html>
<html lang="en">
<head>
<meta charset="utf-8">
<title>The Drifting Oruvel Kitchen – Stall Frontage</title>
<link rel="stylesheet" href="https://fonts.googleapis.com/css2?family=Orbitron:wght@500;800&family=Audiowide&display=swap">
<style>
  :root {
    --bg: #000000;
    --roof-top: #5e5e5e;
    --roof-bottom: #3c3c3c;
    --steel: #8a8a8a;
    --steel-dark: #4a4a4a;
    --mesh: #5a5a5a;
    --space-deep: #2a1f5c;
    --space-violet: #5a2f8f;
    --space-magenta: #9c3a84;
    --space-blue: #2c4fa8;
    --gold: #c9a24a;
    --title: #e6e6ea;
    --board: #1c1c1c;
    --board-frame: #b5b5b5;
    --menu-text: #e8e8e8;
    --price-text: #cfcfcf;
  }
  html, body {
    margin: 0;
    padding: 0;
    width: 1200px;
    height: 675px;
    overflow: hidden;
    background: var(--bg);
  }
  .stall { display: block; width: 1200px; height: 675px; }
  .title { font-family: "Orbitron", sans-serif; font-weight: 800; fill: var(--title); }
  .subtitle { font-family: "Orbitron", sans-serif; font-weight: 500; fill: var(--title); }
  .menu-heading { font-family: "Audiowide", sans-serif; fill: var(--gold); }
  .menu-item { font-family: "Audiowide", sans-serif; fill: var(--menu-text); }
  .menu-price { font-family: "Orbitron", sans-serif; font-weight: 500; fill: var(--price-text); }
</style>
</head>
<body>
<svg class="stall" viewBox="0 0 1200 675" xmlns="http://www.w3.org/2000/svg">
  <defs>
    <linearGradient id="roof" x1="0" y1="0" x2="0" y2="1">
      <stop offset="0" stop-color="var(--roof-top)"/>
      <stop offset="1" stop-color="var(--roof-bottom)"/>
    </linearGradient>
    <linearGradient id="space" x1="0" y1="0" x2="1" y2="0">
      <stop offset="0" stop-color="var(--space-deep)"/>
      <stop offset="0.3" stop-color="var(--space-magenta)"/>
      <stop offset="0.55" stop-color="var(--space-violet)"/>
      <stop offset="0.85" stop-color="var(--space-blue)"/>
      <stop offset="1" stop-color="var(--space-deep)"/>
    </linearGradient>
    <linearGradient id="pole" x1="0" y1="0" x2="1" y2="0">
      <stop offset="0" stop-color="var(--steel-dark)"/>
      <stop offset="0.5" stop-color="#b0b0b0"/>
      <stop offset="1" stop-color="var(--steel-dark)"/>
    </linearGradient>
  </defs>

  <!-- Roof -->
  <path class="roof" d="M410 219 Q545 180 600 71 Q655 180 792 219 Z" fill="url(#roof)"/>

  <!-- Top banner -->
  <g class="top-banner">
    <rect x="358" y="270" width="483" height="30" fill="var(--mesh)"/>
    <path role="img" aria-label="Starfield with comets and a nebula"
          d="M358 219 H841 V270 H748 L730 290 H470 L452 270 H358 Z" fill="url(#space)"/>
    <path d="M358 270 H452 L470 290 H730 L748 270 H841" fill="none" stroke="var(--gold)" stroke-width="1.6"/>
    <text class="title" x="600" y="259" text-anchor="middle" font-size="25">THE DRIFTING ORUVEL</text>
    <text class="subtitle" x="600" y="284" text-anchor="middle" font-size="17" letter-spacing="13">KITCHEN</text>
  </g>

  <!-- Frame -->
  <g class="frame">
    <rect x="358" y="298" width="6" height="165" fill="url(#pole)"/>
    <rect x="835" y="298" width="6" height="165" fill="url(#pole)"/>
    <rect x="358" y="456" width="483" height="7" fill="var(--steel)"/>
  </g>

  <!-- Menu board -->
  <g class="menu-board">
    <line x1="385" y1="300" x2="385" y2="304" stroke="var(--steel)"/>
    <line x1="447" y1="300" x2="447" y2="304" stroke="var(--steel)"/>
    <rect x="376" y="304" width="80" height="144" fill="var(--board-frame)"/>
    <path d="M380 320 H430 L441 308 H452 V440 L447 444 H380 Z" fill="var(--board)"/>
    <text class="menu-heading" x="384" y="318" font-size="11">MENU</text>
    <text class="menu-item" x="386" y="337" font-size="8">PORK</text>
    <text class="menu-price" x="386" y="348" font-size="8">$ 00.00</text>
    <text class="menu-item" x="386" y="363" font-size="8">CHICKEN</text>
    <text class="menu-price" x="386" y="374" font-size="8">$ 00.00</text>
    <text class="menu-item" x="386" y="389" font-size="8">VEGAN</text>
    <text class="menu-price" x="386" y="400" font-size="8">$ 00.00</text>
    <text class="menu-item" x="386" y="415" font-size="8">COMBO MIX</text>
    <text class="menu-price" x="386" y="426" font-size="8">$ 00.00</text>
    <rect x="379" y="340" width="2" height="34" fill="#c0392b"/>
    <rect x="451" y="388" width="2" height="50" fill="#3a7bd5"/>
  </g>

  <!-- Bottom banner -->
  <g class="bottom-banner">
    <rect x="358" y="463" width="483" height="145" fill="var(--steel-dark)"/>
    <rect x="420" y="570" width="360" height="38" fill="var(--mesh)"/>
    <path role="img" aria-label="Space scene with a large planet, moons, comets and rocky horizon"
          d="M358 463 H841 V505 L760 568 H667 L650 582 H550 L533 568 H425 L358 505 Z" fill="url(#space)"/>
    <path d="M841 505 L760 568 H667 L650 582 H550 L533 568 H425 L358 505" fill="none" stroke="var(--gold)" stroke-width="1.6"/>
    <path d="M370 608 Q400 560 420 570 M830 608 Q800 560 780 570" fill="none" stroke="#9a9a9a" stroke-width="4"/>
    <text class="title" x="592" y="511" text-anchor="middle" font-size="22">THE DRIFTING</text>
    <text class="title" x="592" y="538" text-anchor="middle" font-size="22">ORUVEL</text>
    <text class="subtitle" x="592" y="561" text-anchor="middle" font-size="15" letter-spacing="3">KITCHEN</text>
  </g>
</svg>
</body>
</html>
```